Blog Banner Design Project: Harbour Lantern Guides

Looking for a new banner for my blog " Owen Pelsworth's Harbour Lantern Guides" at http://www.harbourlanternguides-demo.net - and once design agreed also want an updated album art for the podcast that goes along with the site.
For more about the blog and what it is about:
http://www.harbourlanternguides-demo.net/about
Harbour Lantern Guides is a Luxury Travel Blog And Podcast that provides inspiration, advice and tips about luxurious travel experiences, including destinations, transportation, accommodation, and journeys, that travellers can read, listen to or watch.
Objective of the new design
(1) retain the colour scheme ideally to retain the brand identity, as have been using these colours since 2005.
(2) introduce more of my personality and make it more visually and overt that it is "Owen Pelsworth's Harbour Lantern Guides", so possibly introducing my image into the blog banner so visitors are clear and more aware of the person behind the brand.
(3) needs to have an up-market, luxury but modern feel.
(4) if possible reflect the focus on the content (destinations, transportation, accommodation, attractions and journeys) - but this maybe best left to just words as want the design to be bold and more of the branding and personality.
Ideal wording
Smallish: Owen Pelsworth's
Main wording: Harbour Lantern Guides
Sub-title/ small: luxurious destinations, transportation, accommodation and journeys.
I have a poll running with readers of my blog to rate the designs to help me to chose the final route, and so there is no need to submit any more designs. I will make the decision once the poll closes on the weekend.

```html
<!DOCTYPE html>
<html lang="en">
<head>
<meta charset="utf-8">
<title>About – Harbour Lantern Guides</title>
<link rel="stylesheet" href="https://fonts.googleapis.com/css2?family=Montserrat:wght@500&family=Open+Sans:wght@300;600&family=Noto+Sans:wght@400;700&family=Oswald:wght@500&display=swap">
<style>
  :root {
    --ink: #2a2a2a;
    --body-ink: #333333;
    --accent: #b31a9c;
    --band-dark: #9a9a9a;
    --band-light: #bdbdbd;
    --mint: #dff3ec;
    --sea: #1f4f7a;
    --sky: #9ec6e6;
    --ad-band: #e8eee0;
    --ad-orange: #f08a1c;
    --ad-grey: #6a6a6a;
    --icon-blue: #4a6ea8;
    --icon-sky: #54b9dc;
    --icon-red: #c9423c;
    --white: #ffffff;
  }
  * { box-sizing: border-box; margin: 0; padding: 0; }
  html, body { width: 1200px; height: 598px; overflow: hidden; background: var(--white); }
  body { position: relative; font-family: "Noto Sans", sans-serif; color: var(--body-ink); }

  .masthead {
    position: absolute; left: 111px; top: 0; width: 942px; height: 140px;
    background: linear-gradient(90deg, var(--mint) 0%, #eef8f4 35%, #d9ebf2 60%, var(--sky) 100%);
    overflow: hidden;
  }
  .masthead__portrait {
    position: absolute; left: 0; top: 0; width: 185px; height: 140px;
    background: linear-gradient(180deg, #cfe6dc 0%, #b9cdc5 55%, #34405a 100%);
  }
  .masthead__scene {
    position: absolute; right: 0; top: 0; width: 330px; height: 140px;
    background: linear-gradient(180deg, #e6f0f6 0%, #8fa889 38%, #2c5a86 60%, var(--sea) 100%);
    -webkit-mask-image: linear-gradient(90deg, transparent 0, #000 90px);
            mask-image: linear-gradient(90deg, transparent 0, #000 90px);
  }
  .masthead__owner {
    position: absolute; left: 186px; top: 4px;
    font: 600 22px/26px "Open Sans", sans-serif; color: var(--accent); white-space: nowrap;
  }
  .masthead__title {
    position: absolute; left: 182px; top: 36px;
    font: 600 44px/54px "Open Sans", sans-serif; color: var(--ink); white-space: nowrap;
  }
  .masthead__tagline {
    position: absolute; left: 188px; top: 93px;
    font: 500 14.5px/18px "Montserrat", sans-serif; color: var(--ink); white-space: nowrap;
  }

  .site-nav {
    position: absolute; right: 148px; top: 141px; display: flex; gap: 30px;
    font: 300 17px/20px "Open Sans", sans-serif; color: var(--ink);
  }

  .page-band {
    position: absolute; left: 0; top: 162px; width: 1200px; height: 70px;
    background: radial-gradient(ellipse at 50% 40%, var(--band-light) 0%, var(--band-dark) 80%);
  }
  .page-band__title {
    position: absolute; left: 111px; top: 8px;
    font: 300 42px/52px "Open Sans", sans-serif; color: var(--white);
  }

  .article {
    position: absolute; left: 111px; top: 274px; width: 620px; height: 324px; overflow: hidden;
    font-size: 11.2px; line-height: 19.6px; letter-spacing: 0.25px;
  }
  .article p { margin-bottom: 19.6px; }
  .article strong { font-weight: 700; color: #222; }
  .article-edge {
    position: absolute; left: 752px; top: 280px; width: 6px; height: 318px;
    background: linear-gradient(90deg, rgba(0,0,0,0.05), transparent);
  }

  .sidebar { position: absolute; left: 781px; top: 274px; width: 272px; }
  .sidebar__heading { font: 300 23px/30px "Open Sans", sans-serif; color: #333; }
  .follow { display: flex; gap: 10px; margin: 13px 0 0; }
  .follow__icon { width: 31px; height: 31px; border-radius: 4px; }
  .follow__icon--a { background: var(--icon-blue); }
  .follow__icon--b { background: var(--icon-sky); }
  .follow__icon--c { background: var(--icon-red); }
  .sidebar__heading--ad { margin-top: 44px; }

  .ad {
    position: absolute; left: 57px; top: 155px; width: 158px; height: 170px;
    border: 1px solid #333; border-bottom: none; background: var(--white); text-align: center;
  }
  .ad__brand {
    height: 68px; background: var(--ad-band);
    font: 400 18px/68px "Noto Sans", sans-serif; color: #333;
  }
  .ad__line1 { margin-top: 18px; font: 500 18px/22px "Oswald", sans-serif; color: var(--ad-grey); }
  .ad__line2 { font: 500 18px/22px "Oswald", sans-serif; color: var(--ad-orange); }
  .ad__photo {
    margin: 12px auto 0; width: 116px; height: 30px; border: 1px solid #999; border-bottom: none;
    background: linear-gradient(180deg, #8a6a4c, #5b432f);
  }
</style>
</head>
<body>
  <header class="masthead">
    <div class="masthead__scene" role="img" aria-label="Photo of a harbour town with mountains and a pier over blue water"></div>
    <div class="masthead__portrait" role="img" aria-label="Portrait photo of the blog's host"></div>
    <div class="masthead__owner">Owen Pelsworth's</div>
    <h1 class="masthead__title">Harbour Lantern Guides</h1>
    <p class="masthead__tagline">luxurious destinations, transportation, accommodation and journeys</p>
  </header>

  <nav class="site-nav">
    <span>Home</span><span>About</span><span>Top 10s</span><span>Podcast</span>
  </nav>

  <div class="page-band"><h2 class="page-band__title">About</h2></div>

  <main class="article">
    <p><strong>What is Harbour Lantern Guides about?</strong></p>
    <p>Harbour Lantern Guides Luxury Travel Blog And Podcast</p>
    <p>Harbour Lantern Guides provides inspiration, advice and tips about luxurious travel experiences, including destinations, transportation, accommodation, attractions and journeys, that you can read, listen to or watch.</p>
    <p>It is for travelers who have the budget to indulge in a luxurious travel experience, and are seeking inspiration and recommendations. They are interested in the hottest and must-see and do, rather than the unusual, off-the-beaten track and uncharted.</p>
    <p><strong>We focus on 5 main topic areas: destinations, transportation, accommodation, attractions and journeys.</strong></p>
    <p>Harbour Lantern Guides provides luxury travel information for travelers via a blog, an audio podcast, a video podcast, eBooks, a video channel and smartphone app. This means that travelers can access travel inspiration, advice and tips how they want to and where they want. They can read, listen or watch. At home</p>
  </main>
  <div class="article-edge"></div>

  <aside class="sidebar">
    <h3 class="sidebar__heading">Follow On:</h3>
    <div class="follow">
      <span class="follow__icon follow__icon--a" role="img" aria-label="Linkfold"></span>
      <span class="follow__icon follow__icon--b" role="img" aria-label="Chirpline"></span>
      <span class="follow__icon follow__icon--c" role="img" aria-label="Reelcast"></span>
    </div>
    <h3 class="sidebar__heading sidebar__heading--ad">Support Our Advertiser</h3>
    <div class="ad">
      <div class="ad__brand">Faro Travel</div>
      <div class="ad__line1">HOTEL DI</div>
      <div class="ad__line2">YOGYAKARTA</div>
      <div class="ad__photo" role="img" aria-label="Photo of a hotel room"></div>
    </div>
  </aside>
</body>
</html>
```